"Lemonade on Sundays" needs a cool album cover :)

We need a digital CD cover for a new comedy album called "Lemonade on Sundays" by Denise Holloway. We would like for it to have a retro/vintage feel for the artwork, inspired by the 60s & 70s. The colors should be fun and bright. We want the cover to be bright and eye-catching, and have the feel of a vinyl album cover from the 1960s/70s.
UPDATE: Since this is a digital album, and not a physical CD, we only need the artwork in a square format as it will not be printed on a CD itself. The artwork will be used to promote the album on social media, etc.
Target Market(s)
Anyone listening to comedy, Age demographic 40 and over
Industry/Entity Type
Comedy, Entertainment
Font styles to use
Other font styles liked:
- Retro fonts
Requirements
Must have
- Album Title: Lemonade on Sundays, Artist Name: Denise Holloway, Artwork or photos depicting cocktails & pajamas
Nice to have
- Vintage / Retro feel & fonts
Should not have
- Even though this is a comedy album, we do not want any comedy references on the cover such as microphones, laughing faces, etc.

```html
<!DOCTYPE html>
<html lang="en">
<head>
<meta charset="utf-8">
<title>Lemonade on Sundays – Denise Holloway</title>
<link rel="stylesheet" href="https://fonts.googleapis.com/css2?family=Shrikhand&family=Titan+One&display=swap">
<style>
  :root {
    --blush: #f3dfd6;
    --teal: #009e8e;
    --magenta: #ec008c;
    --navy: #00005a;
    --citron: #e0cf22;
    --leaf: #0a9a1e;
    --marigold: #f0b842;
    --sky: #b9d9dd;
    --orange: #e8720c;
    --brown: #8a4a10;
    --candy: #fb8cb4;
    --slate: #a8b6cc;
  }
  html, body {
    margin: 0;
    padding: 0;
    overflow: hidden;
    background: var(--blush);
  }
  .cover {
    position: relative;
    width: 1200px;
    height: 1200px;
    background: var(--blush);
    overflow: hidden;
  }
  .art {
    position: absolute;
    display: block;
  }
  .art--moon { left: 142px; top: 76px; width: 100px; height: 100px; border-radius: 50%; background: var(--marigold); }
  .art--star { width: 40px; height: 40px; border-radius: 50%; background: var(--marigold); }
  .art--star-top { left: 558px; top: 62px; }
  .art--star-left { left: 58px; top: 484px; }
  .art--star-right { left: 1074px; top: 480px; }
  .art--star-title { left: 448px; top: 578px; background: var(--magenta); }
  .art--cloud { border-radius: 60px; background: var(--sky); }
  .art--cloud-small { left: 318px; top: 164px; width: 150px; height: 94px; }
  .art--cloud-large { left: 912px; top: 50px; width: 200px; height: 122px; }
  .art--glass {
    left: 702px; top: 813px; width: 92px; height: 162px;
    border-radius: 8px;
    background: linear-gradient(90deg, var(--magenta), var(--navy), var(--teal));
  }
  .art--pajamas {
    left: 888px; top: 813px; width: 275px; height: 272px;
    border-radius: 12px;
    background: linear-gradient(120deg, var(--slate), var(--candy));
  }
  .title {
    position: absolute;
    left: 0; top: 0;
    width: 1200px; height: 900px;
  }
  .title text {
    font-family: "Shrikhand", serif;
  }
  .title__layer { mix-blend-mode: multiply; }
  .title__main--teal { fill: var(--teal); }
  .title__main--magenta { fill: var(--magenta); }
  .title__joint--leaf { fill: var(--leaf); }
  .title__joint--citron { fill: var(--citron); }
  .title__sub--citron { fill: var(--citron); }
  .title__sub--magenta { fill: var(--magenta); }
  .credit {
    position: absolute;
    left: 210px;
    top: 1020px;
    margin: 0;
    font-family: "Titan One", sans-serif;
    font-weight: 400;
    line-height: 1;
    display: flex;
    align-items: baseline;
    gap: 24px;
    white-space: nowrap;
  }
  .credit__by {
    font-size: 30px;
    color: var(--brown);
    letter-spacing: 1px;
  }
  .credit__artist {
    font-size: 58px;
    color: var(--orange);
    letter-spacing: 1px;
  }
</style>
</head>
<body>
  <main class="cover">
    <div class="art art--moon" role="img" aria-label="Crescent moon illustration"></div>
    <div class="art art--star art--star-top" role="img" aria-label="Small star illustration"></div>
    <div class="art art--star art--star-left" role="img" aria-label="Small star illustration"></div>
    <div class="art art--star art--star-right" role="img" aria-label="Small star illustration"></div>
    <div class="art art--cloud art--cloud-small" role="img" aria-label="Outlined cloud illustration"></div>
    <div class="art art--cloud art--cloud-large" role="img" aria-label="Outlined cloud illustration"></div>

    <svg class="title" viewBox="0 0 1200 900" role="heading" aria-level="1" aria-label="Lemonade on Sundays">
      <defs>
        <path id="arc-main" d="M110 480 Q 600 470 1080 360"/>
        <path id="arc-sub" d="M130 770 Q 600 740 1080 660"/>
      </defs>

      <g class="title__layer">
        <text class="title__main--teal" font-size="190" transform="translate(-10,-22)">
          <textPath href="#arc-main" textLength="950" lengthAdjust="spacingAndGlyphs">Lemonade</textPath>
        </text>
      </g>
      <g class="title__layer">
        <text class="title__main--magenta" font-size="190" transform="translate(12,22)">
          <textPath href="#arc-main" textLength="950" lengthAdjust="spacingAndGlyphs">Lemonade</textPath>
        </text>
      </g>

      <text class="title__joint--citron" x="742" y="518" font-size="58">on</text>
      <text class="title__joint--leaf" x="736" y="506" font-size="58">on</text>

      <text class="title__sub--citron" font-size="210" transform="translate(-40,44)">
        <textPath href="#arc-sub" textLength="940" lengthAdjust="spacingAndGlyphs">Sundays</textPath>
      </text>
      <text class="title__sub--magenta" font-size="210">
        <textPath href="#arc-sub" textLength="940" lengthAdjust="spacingAndGlyphs">Sundays</textPath>
      </text>
    </svg>

    <div class="art art--star art--star-title" role="img" aria-label="Small star illustration"></div>
    <div class="art art--glass" role="img" aria-label="Martini glass illustration"></div>
    <div class="art art--pajamas" role="img" aria-label="Folded striped and starry pajama trousers illustration"></div>

    <p class="credit">
      <span class="credit__by">BY:</span>
      <span class="credit__artist">DENISE HOLLOWAY</span>
    </p>
  </main>
</body>
</html>
```